Consulting, Investors, Joint Venture Website

Founded in April 2018, Marendo Consultants Limited (MCL) is an advisory consulting firm specializing in engaging investors in business ventures in Tanzania.
With extensive experience in construction, energy, oil and gas and the legal professions, our team assembles our expertise that allows foreign investors to set foot and flourish in the Tanzanian market.
MCL is locally owned, founded and registered. Our shareholders are cultured Tanzanian citizens with extensive corporate experience in South Africa, Tanzania, United Kingdom and the United States.

Our mission is to provide responsive and unrivalled professional advice from learned and experienced professionals versed in the local market, with an understanding of the cultural and logistical challenges faced by foreign investors.

Our vision is to provide a complete investor’s package that initiates with company registration, compliance and documentation services and ultimately operational facilitation services.

Target Market(s)

Foreign Investors, International companies

Industry/Entity Type

Business Consultant

Number of Pages Required

5+ page

Requirements
Must have
• It will be 5 pages - Home, About Us, Services, Portfolio, Contact Us
Nice to have
• if it can look like https://www.plorvex.example/
• or https://www.dunetri.example or http://www.quillbrook.example/

```html
<!DOCTYPE html>
<html lang="en">
<head>
<meta charset="utf-8">
<title>Marendo Consultants Limited – Professional Business Consulting</title>
<link rel="stylesheet" href="https://fonts.googleapis.com/css2?family=Roboto:wght@300;400;500;700&family=Open+Sans:wght@400;600&display=swap">
<style>
:root{
  --blue:#0b6bb5;
  --blue-dark:#0a4f8a;
  --blue-light:#2ea3e0;
  --orange:#f39c24;
  --salmon:#e4807a;
  --pink:#f2b6b0;
  --text:#5a5f66;
  --heading:#1c5d9c;
  --line:#d9dde3;
  --bg-soft:#eef2f7;
  --white:#ffffff;
}
*{margin:0;padding:0;box-sizing:border-box}
html,body{width:1200px;height:4675px;overflow:hidden;background:var(--white)}
body{font-family:"Open Sans",Arial,sans-serif;color:var(--text);font-size:15px}
.page{position:relative;width:1200px;height:4675px}
section,header,footer{position:relative;width:1200px;overflow:hidden}
.section-title{font-family:"Roboto",Arial,sans-serif;font-weight:400;font-size:34px;text-align:center;color:var(--heading);letter-spacing:1px}
.section-title span{color:var(--orange)}
.title-rule{display:block;margin:14px auto 0;width:120px;height:8px}

/* nav */
.site-header{height:110px;display:flex;align-items:center;justify-content:space-between;padding:0 0 0 40px;border-bottom:1px solid var(--line)}
.brand{display:flex;align-items:center;gap:10px;font-family:"Roboto",sans-serif;font-weight:700;font-size:28px;color:var(--blue);letter-spacing:1px}
.brand-mark{width:26px;height:26px;background:var(--blue)}
.main-nav{display:flex;height:110px;align-items:center;padding-right:10px}
.main-nav a{font-family:"Roboto",sans-serif;font-size:16px;color:var(--text);text-decoration:none;padding:0 20px;height:64px;line-height:64px}
.main-nav a.active{background:var(--orange);color:var(--white)}

/* hero */
.hero{height:560px}
.hero-bg{position:absolute;inset:0;background:linear-gradient(115deg,#0a4f8a 0%,#0b6bb5 40%,#2ea3e0 70%,#7fc6ee 100%)}
.hero-accent{position:absolute;inset:0}
.hero-copy{position:absolute;left:60px;top:110px;color:var(--white);width:600px}
.hero-copy h1{font-family:"Roboto",sans-serif;font-weight:500;font-size:38px;white-space:nowrap;margin-bottom:14px}
.hero-copy .tagline{font-family:"Roboto",sans-serif;font-size:16px;letter-spacing:1px;text-align:center;margin-bottom:40px}
.hero-copy p{font-size:18px;line-height:28px;text-align:center}
.btn-outline{display:block;margin:40px auto 0;width:150px;height:46px;border:2px solid var(--white);border-radius:24px;color:var(--white);text-align:center;line-height:42px;font-family:"Roboto",sans-serif;font-size:14px}

/* about */
.about{height:525px;padding-top:90px;text-align:center}
.about p{width:1000px;margin:0 auto;font-size:16px;line-height:28px}
.about .title-rule{margin-bottom:40px}
.about p + p{margin-top:36px}

/* vision mission */
.vision-mission{height:660px}
.photo{position:absolute;top:0;height:430px}
.photo-left{left:0;width:592px;background:linear-gradient(135deg,#e9e4dc,#c9bfb3 60%,#8d7f72)}
.photo-right{left:608px;width:592px;background:linear-gradient(135deg,#d8d2ca,#9a8f84 55%,#3f3a37)}
.vm-box{position:absolute;top:300px;width:458px;height:310px;color:var(--white);text-align:center;padding:40px 46px}
.vm-box h3{font-family:"Roboto",sans-serif;font-weight:300;font-size:34px;letter-spacing:1px}
.vm-box h3 b{font-weight:500}
.vm-box .title-rule{margin:12px auto 22px}
.vm-box p{font-size:15px;line-height:25px}
.vision-box{left:134px;background:linear-gradient(160deg,#1673c2,#0a4f8a)}
.mission-box{left:608px;background:linear-gradient(160deg,#ee9a8f,#d9655f)}

/* services */
.services-head{height:140px;padding-top:50px}
.services{height:880px}
.services-band{position:absolute;left:0;right:0;top:40px;height:640px;background:linear-gradient(90deg,#e9eef4 0%,#cfe0ef 30%,#2a8fd6 55%,#f1c2bc 80%,#e98f86 100%)}
.service-card{position:absolute;width:280px;height:560px;background:var(--white);box-shadow:0 6px 20px rgba(0,0,0,.15);text-align:center}
.service-card .thumb{height:240px}
.service-card h4{font-family:"Roboto",sans-serif;font-weight:700;font-size:19px;color:var(--blue-dark);margin:34px 0 14px;letter-spacing:.5px}
.service-card p{font-size:15px;line-height:24px;padding:0 30px}
.btn-solid{display:inline-block;margin-top:36px;background:var(--blue);color:var(--white);font-family:"Roboto",sans-serif;font-weight:500;font-size:14px;padding:12px 18px}
.card-1{left:16px;top:0}
.card-2{left:312px;top:220px}
.card-3{left:608px;top:0}
.card-4{left:904px;top:220px}
.thumb-construction{background:linear-gradient(180deg,#8cc7ea,#d8a15c)}
.thumb-energy{background:linear-gradient(180deg,#f2b04a,#7a5a2a)}
.thumb-oil{background:linear-gradient(180deg,#2a4f86,#d39a3d)}
.thumb-legal{background:linear-gradient(180deg,#2b2320,#b5895a)}

/* why choose us */
.why{height:820px;background:var(--bg-soft)}
.why-left{position:absolute;left:30px;top:90px;width:460px}
.why-left .section-title{text-align:center}
.accordion{margin-top:50px}
.acc-item{background:var(--white);border:1px solid var(--line);height:46px;display:flex;align-items:center;justify-content:space-between;padding:0 18px;font-size:15px;margin-bottom:10px}
.acc-item.open{border-color:var(--white)}
.acc-body{font-size:14px;line-height:22px;padding:10px 18px 24px;margin-bottom:10px}
.acc-item svg{width:12px;height:12px}
.why-actions{margin-top:28px;display:flex;align-items:center;gap:30px}
.why-actions .btn-solid{margin:0}
.phone{display:flex;align-items:center;gap:12px;font-size:15px}
.why-right{position:absolute;left:520px;top:0;width:680px;height:820px}
.step{position:absolute;display:flex;gap:18px;width:470px}
.step-icon{flex:0 0 80px;height:80px;border-radius:50%;display:flex;align-items:center;justify-content:center}
.step h5{font-family:"Roboto",sans-serif;font-weight:500;font-size:17px;color:#333;margin:8px 0 6px}
.step p{font-size:14px;line-height:21px}
.step-1{left:200px;top:130px}
.step-2{left:130px;top:300px}
.step-3{left:70px;top:470px}
.step-4{left:20px;top:640px}
.ic-dark{background:#444a52}
.ic-orange{background:#ee6b3a}
.ic-green{background:#3c9a3a}
.ic-blue{background:var(--blue)}

/* contact */
.contact{height:880px}
.map{position:absolute;left:0;top:60px;width:590px;height:760px;background:linear-gradient(135deg,#eef0e8,#dfe6d9 50%,#cfd9e0)}
.contact-card{position:absolute;left:47px;top:440px;width:514px;height:300px;background:linear-gradient(180deg,#1777c4,#0a4f8a);color:var(--white);padding:36px 50px}
.contact-card h4{font-family:"Roboto",sans-serif;font-weight:500;font-size:22px;text-align:center;letter-spacing:1px}
.contact-card .title-rule{margin:10px auto 28px}
.contact-card li{list-style:none;display:flex;align-items:center;gap:14px;font-size:15px;margin-bottom:20px}
.contact-form{position:absolute;left:650px;top:120px;width:500px}
.contact-form h3{font-family:"Roboto",sans-serif;font-weight:400;font-size:30px;color:var(--heading)}
.contact-form h3 span{color:var(--orange)}
.contact-form .title-rule{margin:12px 0 40px}
.field{border-bottom:1px solid #c7ccd3;height:62px;display:flex;align-items:flex-end;padding-bottom:10px;font-size:15px;color:#444}
.field.message{height:140px;align-items:flex-start;padding-top:34px}
.contact-form .btn-solid{margin-top:44px;padding:14px 38px}

/* footer */
.site-footer{height:100px;border-top:6px solid transparent;border-image:linear-gradient(90deg,var(--pink),var(--blue-light)) 1}
.footer-links{position:absolute;left:30px;top:26px;font-size:14px;color:var(--blue)}
.footer-copy{position:absolute;left:30px;top:54px;font-size:13px}
.social{position:absolute;right:30px;top:28px;display:flex;gap:14px}
.social span{width:34px;height:34px;background:var(--blue);display:block}
</style>
</head>
<body>
<div class="page">

<header class="site-header">
  <div class="brand"><span class="brand-mark"></span>MARENDO</div>
  <nav class="main-nav">
    <a class="active">Home</a><a>About Us</a><a>Services</a><a>Portfolio</a><a>Contact Us</a>
  </nav>
</header>

<section class="hero">
  <div class="hero-bg" role="img" aria-label="Business team photograph in blue tones"></div>
  <svg class="hero-accent" width="1200" height="560" viewBox="0 0 1200 560">
    <polygon points="520,560 1200,380 1200,560" fill="#f2b6b0" opacity=".55"/>
    <polygon points="760,560 1200,460 1200,560" fill="#ffffff" opacity=".6"/>
  </svg>
  <div class="hero-copy">
    <h1>Professional Business Consulting</h1>
    <div class="tagline">INNOVATIVE SOLUTIONS AND STRATEGIC PLANNING</div>
    <p>We help global leaders with their organization's most critical issues and opportunities. Together, we create enduring change and results.</p>
    <span class="btn-outline">CONTACT US</span>
  </div>
</section>

<section class="about">
  <h2 class="section-title">ABOUT <span>US</span></h2>
  <svg class="title-rule" viewBox="0 0 120 8"><line x1="0" y1="4" x2="120" y2="4" stroke="#f39c24" stroke-width="2"/><circle cx="60" cy="4" r="4" fill="#1c5d9c"/></svg>
  <p>Founded in April 2018, Marendo Consultants Limited (MCL) is an advisory consulting firm specializing in engaging investors in business ventures in Tanzania. With extensive experience in construction, energy, oil and gas and the legal professions, our team assembles our expertise that allows foreign investors to set foot and flourish in the Tanzanian market.</p>
  <p>MCL is locally owned, founded and registered. Our shareholders are cultured Tanzanian citizens with extensive corporate experience in South Africa, Tanzania, United Kingdom and the United States.</p>
</section>

<section class="vision-mission">
  <div class="photo photo-left" role="img" aria-label="Smiling businesswoman working at a laptop"></div>
  <div class="photo photo-right" role="img" aria-label="Consultant in a meeting with a client"></div>
  <div class="vm-box vision-box">
    <h3>OUR <b>VISION</b></h3>
    <svg class="title-rule" viewBox="0 0 120 8"><line x1="0" y1="4" x2="120" y2="4" stroke="#fff" stroke-width="2"/><circle cx="60" cy="4" r="4" fill="#f39c24"/></svg>
    <p>Our vision is to provide a complete investor's package that initiates with company registration, compliance and documentation services and ultimately operational facilitation services.</p>
  </div>
  <div class="vm-box mission-box">
    <h3>OUR <b>MISSION</b></h3>
    <svg class="title-rule" viewBox="0 0 120 8"><line x1="0" y1="4" x2="120" y2="4" stroke="#fff" stroke-width="2"/><circle cx="60" cy="4" r="4" fill="#1c5d9c"/></svg>
    <p>Our mission is to provide responsive and unrivalled professional advice from learned and experienced professionals versed in the local market, with an understanding of the cultural and logistical challenges faced by foreign investors.</p>
  </div>
</section>

<div class="services-head">
  <h2 class="section-title">OUR <span>SERVICES</span></h2>
  <svg class="title-rule" viewBox="0 0 120 8"><line x1="0" y1="4" x2="120" y2="4" stroke="#f39c24" stroke-width="2"/><circle cx="60" cy="4" r="4" fill="#1c5d9c"/></svg>
</div>

<section class="services">
  <div class="services-band"></div>
  <article class="service-card card-1">
    <div class="thumb thumb-construction" role="img" aria-label="Construction site with cranes"></div>
    <h4>CONSTRUCTION</h4>
    <p>This global consulting firm bring big ideas and challenge the norm.</p>
    <span class="btn-solid">FIND OUT MORE</span>
  </article>
  <article class="service-card card-2">
    <div class="thumb thumb-energy" role="img" aria-label="Power lines at sunset"></div>
    <h4>ENERGY</h4>
    <p>This global consulting firm bring big ideas and challenge the norm.</p>
    <span class="btn-solid">FIND OUT MORE</span>
  </article>
  <article class="service-card card-3">
    <div class="thumb thumb-oil" role="img" aria-label="Oil refinery lit at night"></div>
    <h4>OIL &amp; GAS</h4>
    <p>This global consulting firm bring big ideas and challenge the norm.</p>
    <span class="btn-solid">FIND OUT MORE</span>
  </article>
  <article class="service-card card-4">
    <div class="thumb thumb-legal" role="img" aria-label="Scales of justice on a desk"></div>
    <h4>LEGAL PROFESSIONS</h4>
    <p>This global consulting firm bring big ideas and challenge the norm.</p>
    <span class="btn-solid">FIND OUT MORE</span>
  </article>
</section>

<section class="why">
  <div class="why-left">
    <h2 class="section-title">WHY <span>CHOOSE US</span></h2>
    <svg class="title-rule" viewBox="0 0 120 8"><line x1="0" y1="4" x2="120" y2="4" stroke="#f39c24" stroke-width="2"/><circle cx="60" cy="4" r="4" fill="#1c5d9c"/></svg>
    <div class="accordion">
      <div class="acc-item open">We can help you to grow your business<svg viewBox="0 0 12 12"><polygon points="0,9 12,9 6,2" fill="#444"/></svg></div>
      <div class="acc-body">There are many variations of passages of Lorem Ipsum available but the about majority a have suffered alteration in some form by injected humour or that a randomised even slightly believable.</div>
      <div class="acc-item">We can help you to grow your business<svg viewBox="0 0 12 12"><polygon points="0,3 12,3 6,10" fill="#444"/></svg></div>
      <div class="acc-item">We can help you to grow your business<svg viewBox="0 0 12 12"><polygon points="0,3 12,3 6,10" fill="#444"/></svg></div>
      <div class="acc-item">We can help you to grow your business<svg viewBox="0 0 12 12"><polygon points="0,3 12,3 6,10" fill="#444"/></svg></div>
    </div>
    <div class="why-actions">
      <span class="btn-solid">CONTACT US</span>
      <div class="phone"><svg width="30" height="30" viewBox="0 0 30 30"><circle cx="15" cy="15" r="14" fill="#fff" stroke="#c7ccd3"/><path d="M11 9l3 3-2 2c1 2 2 3 4 4l2-2 3 3-2 2c-5 0-10-5-10-10z" fill="#555"/></svg>02-555-014 7070</div>
    </div>
  </div>
  <div class="why-right">
    <div class="step step-1"><div class="step-icon ic-dark"><svg width="34" height="34" viewBox="0 0 34 34"><circle cx="17" cy="17" r="8" fill="none" stroke="#fff" stroke-width="3"/></svg></div><div><h5>Outstanding Communication</h5><p>Is your marketing working? Our marketing consulting services help you determine who your ideal client is, narrow your focus and target.</p></div></div>
    <div class="step step-2"><div class="step-icon ic-orange"><svg width="34" height="34" viewBox="0 0 34 34"><path d="M8 18l6 6 12-14" fill="none" stroke="#fff" stroke-width="3"/></svg></div><div><h5>Problem Solving Support</h5><p>Feeling overwhelmed? Our business consulting services help business owners clarify their processes, goals, and milestones. We help you figure out how to take back control of your business.</p></div></div>
    <div class="step step-3"><div class="step-icon ic-green"><svg width="34" height="34" viewBox="0 0 34 34"><path d="M17 28V12M10 16l7-8 7 8" fill="none" stroke="#fff" stroke-width="3"/></svg></div><div><h5>Marketing Consulting</h5><p>Is your marketing working? Our marketing consulting services help you determine who your ideal client is, narrow your focus and who you really want to reach. We help you reach the right people at the right time.</p></div></div>
    <div class="step step-4"><div class="step-icon ic-blue"><svg width="34" height="34" viewBox="0 0 34 34"><rect x="7" y="9" width="20" height="14" fill="none" stroke="#fff" stroke-width="3"/><line x1="12" y1="27" x2="22" y2="27" stroke="#fff" stroke-width="3"/></svg></div><div><h5>Business Consulting</h5><p>Feeling overwhelmed? Our business consulting services help business owners clarify their processes, goals, and milestones. We help you figure out how to take back control of your business and reclaim your life.</p></div></div>
  </div>
</section>

<section class="contact">
  <div class="map" role="img" aria-label="Street map showing the office location"></div>
  <div class="contact-card">
    <h4>CONTACT US</h4>
    <svg class="title-rule" viewBox="0 0 120 8"><line x1="0" y1="4" x2="120" y2="4" stroke="#fff" stroke-width="2"/><circle cx="60" cy="4" r="4" fill="#f39c24"/></svg>
    <ul>
      <li><svg width="16" height="20" viewBox="0 0 16 20"><path d="M8 0a7 7 0 0 1 7 7c0 5-7 13-7 13S1 12 1 7a7 7 0 0 1 7-7z" fill="#fff"/><circle cx="8" cy="7" r="2.5" fill="#0a4f8a"/></svg>1420 Larkspur Avenue, Suite 210, GA 30000, USA</li>
      <li><svg width="16" height="16" viewBox="0 0 16 16"><path d="M2 1l4 4-2 2c1 2 3 4 5 5l2-2 4 4-2 2C6 16 0 10 0 3z" fill="#fff"/></svg>Call Us: +1 555 014 2290</li>
      <li><svg width="18" height="14" viewBox="0 0 18 14"><rect x="0" y="0" width="18" height="14" fill="#fff"/><path d="M0 0l9 8 9-8" fill="none" stroke="#0a4f8a" stroke-width="1.5"/></svg>Mail: info@marendo.example</li>
    </ul>
  </div>
  <form class="contact-form">
    <h3>PLEASE FILL UP <span>THE FORM</span></h3>
    <svg class="title-rule" viewBox="0 0 120 8"><line x1="0" y1="4" x2="120" y2="4" stroke="#f39c24" stroke-width="2"/><circle cx="60" cy="4" r="4" fill="#1c5d9c"/></svg>
    <div class="field">First Name</div>
    <div class="field">Phone Number</div>
    <div class="field">Email Address</div>
    <div class="field message">Message</div>
    <span class="btn-solid">SUBMIT</span>
  </form>
</section>

<footer class="site-footer">
  <div class="footer-links">Home | About Us | Services | Portfolio | Contact Us</div>
  <div class="footer-copy">© Copyright 2018 . All rights reserved</div>
  <div class="social"><span></span><span></span><span></span></div>
</footer>

</div>
</body>
</html>
```